Residential & commercial landscaping company

Updated business cards for commercial and landscaping company. We would like to keep out logo, but just need a more updated business card.

```html
<!DOCTYPE html>
<html lang="en">
<head>
<meta charset="utf-8">
<title>TerraVista Business Cards</title>
<link rel="stylesheet" href="https://fonts.googleapis.com/css2?family=Arimo:wght@400;700&family=Tinos:wght@700&display=swap">
<style>
  :root {
    --backdrop: #3a3a3a;
    --backdrop-edge: #1c1c1c;
    --leaf-light: #4cc94c;
    --leaf-mid: #1fa83a;
    --leaf-deep: #0a7a32;
    --leaf-wash: #dff2dc;
    --accent-green: #3cc23c;
    --ink: #111111;
    --paper: #ffffff;
  }
  * { box-sizing: border-box; margin: 0; padding: 0; }
  html, body { width: 1200px; height: 1015px; overflow: hidden; }
  body {
    background: radial-gradient(ellipse at 45% 40%, var(--backdrop) 0%, var(--backdrop-edge) 100%);
    font-family: "Arimo", Arial, sans-serif;
    position: relative;
  }
  .card {
    position: absolute;
    left: 320px;
    width: 560px;
    height: 320px;
    overflow: hidden;
    box-shadow: 0 10px 30px rgba(0,0,0,0.55);
  }
  .card-front { top: 150px; }
  .card-back { top: 545px; background: var(--paper); }

  .front-foliage {
    position: absolute; inset: 0;
    background:
      radial-gradient(ellipse at 55% 50%, rgba(10,110,40,0.35) 0%, rgba(10,110,40,0) 60%),
      linear-gradient(160deg, var(--leaf-light) 0%, var(--leaf-mid) 50%, var(--leaf-deep) 100%);
  }
  .front-name {
    position: absolute; left: 0; right: 0; top: 50%;
    transform: translateY(-50%);
    text-align: center;
    color: var(--paper);
    font-weight: 700;
    font-size: 64px;
    letter-spacing: -1px;
  }

  .back-foliage {
    position: absolute; right: 0; top: 0;
    width: 230px; height: 250px;
    background: radial-gradient(ellipse at 60% 45%, var(--leaf-wash) 0%, rgba(223,242,220,0.6) 55%, rgba(255,255,255,0) 75%);
  }
  .brand {
    position: absolute; left: 30px; top: 118px;
    display: flex; align-items: center; gap: 10px;
  }
  .brand-mark { width: 34px; height: 34px; background: var(--leaf-mid); }
  .brand-name {
    font-weight: 700; font-size: 38px; color: var(--ink); letter-spacing: -1px;
  }
  .contact {
    position: absolute; left: 292px; top: 108px;
  }
  .contact-name {
    font-family: "Tinos", "Times New Roman", serif;
    font-weight: 700; font-size: 24px; color: var(--accent-green);
  }
  .contact-role { font-size: 13px; color: var(--ink); margin-bottom: 12px; }
  .contact-line {
    display: flex; align-items: center; gap: 7px;
    font-size: 13px; color: var(--ink); line-height: 19px;
  }
  .contact-line svg { width: 13px; height: 13px; flex: none; }
</style>
</head>
<body>
  <section class="card card-front">
    <div class="front-foliage" role="img" aria-label="Tree canopy illustration in layered greens"></div>
    <div class="front-name">TerraVista</div>
  </section>

  <section class="card card-back">
    <div class="back-foliage" role="img" aria-label="Faint tree illustration in pale green"></div>
    <div class="brand">
      <span class="brand-mark"></span>
      <span class="brand-name">TerraVista</span>
    </div>
    <div class="contact">
      <div class="contact-name">Daniel Harlow Jr.</div>
      <div class="contact-role">Project Manager</div>
      <div class="contact-line">
        <svg viewBox="0 0 16 16" aria-hidden="true"><path fill="#3cc23c" d="M3.5 1.5l2.3 2.8-1.3 1.6a9 9 0 0 0 5.6 5.6l1.6-1.3 2.8 2.3-1.6 2A12 12 0 0 1 1.5 3.1z"/></svg>
        <span>555-201-0148 ext.204</span>
      </div>
      <div class="contact-line">
        <svg viewBox="0 0 16 16" aria-hidden="true"><rect x="4" y="1" width="8" height="4" fill="#3cc23c"/><rect x="1" y="6" width="14" height="6" rx="1" fill="#3cc23c"/><rect x="4" y="10" width="8" height="5" fill="#fff" stroke="#3cc23c" stroke-width="1.5"/></svg>
        <span>555-317-0962</span>
      </div>
      <div class="contact-line">
        <svg viewBox="0 0 16 16" aria-hidden="true"><rect x="1" y="3" width="14" height="10" fill="#3cc23c"/><path d="M1 3l7 6 7-6" fill="none" stroke="#fff" stroke-width="1.4"/></svg>
        <span>dan@TerraVistaGrounds.com</span>
      </div>
    </div>
  </section>
</body>
</html>
```